Progressive Flow Chart

Looking for a progressive flow chart centered and branching off. They all build on each other 1-3. There will be 3 different pages.

Target Market(s)

Business Owners - High Net worth Individuals

Industry/Entity Type

Finance & Business Consulting

Font styles to use
Serif

Colors
0054AA
0677BA
7BADD7
CADEEF
E8F1F8
0094D4
00A9DD
6FCCEA
C7EBF8
E9F6FB
00AB8E
00BBA5
67D7C9
C6EFE9
E9F9F6

Requirements
Nice to have
• Clean, simple, and approachable.
Should not have
• Very Busy

```html
<!DOCTYPE html>
<html lang="en">
<head>
<meta charset="utf-8">
<title>Progressive Flow Chart</title>
<link href="https://fonts.googleapis.com/css2?family=Quicksand:wght@500;600;700&display=swap" rel="stylesheet">
<style>
  :root {
    --bg: #252525;
    --ink: #222a2e;
    --white: #ffffff;
    --grey-box: #e1e2e3;
    --grey-badge: #d4d6d8;
    --blue-soft: #7badd7;
    --blue-light: #8ec2ee;
    --sky: #00a9dd;
    --teal: #00bba5;
    --teal-deep: #00ab8e;
    --mint: #1af2b0;
    --ring: #1f6b52;
    --flow: rgba(220, 222, 224, 0.62);
  }
  * { box-sizing: border-box; margin: 0; padding: 0; }
  html, body { width: 1200px; height: 848px; overflow: hidden; background: var(--bg); }
  .canvas {
    position: relative; width: 1200px; height: 848px; overflow: hidden;
    background: var(--bg);
    font-family: "Quicksand", "Helvetica Neue", Arial, sans-serif;
    color: var(--ink);
  }
  .title {
    position: absolute; top: 78px; left: 0; width: 1237px; text-align: center;
    font-size: 34px; font-weight: 700; letter-spacing: 0.5px; color: var(--white);
  }
  .title .accent { color: var(--sky); margin-left: 14px; }
  .brand {
    position: absolute; top: 58px; left: 1010px; width: 130px; text-align: center;
  }
  .brand-dot {
    display: block; width: 40px; height: 40px; margin: 0 auto 10px;
    border-radius: 50%; background: var(--sky);
  }
  .brand-name { font-size: 15px; font-weight: 600; color: var(--sky); letter-spacing: 0.5px; }
  .flows { position: absolute; inset: 0; }
  .box {
    position: absolute; width: 180px; height: 106px; border-radius: 6px;
    display: flex; flex-direction: column; align-items: center; justify-content: center;
    text-align: center; font-weight: 700; font-size: 16px; line-height: 1.2;
    box-shadow: 0 4px 10px rgba(0,0,0,0.45);
  }
  .box--strategy { background: var(--grey-box); }
  .box--bank, .box--insurance { background: linear-gradient(160deg, var(--blue-light), var(--blue-soft)); }
  .box--entity { background: var(--mint); }
  .box .note { font-size: 12px; font-weight: 500; margin-top: 8px; line-height: 1.3; }
  .box--bank { justify-content: flex-start; padding-top: 22px; }
  .box--business { justify-content: flex-start; padding-top: 26px; }
  .box--business .note { margin-top: 4px; }
  .badge {
    position: absolute; width: 40px; height: 40px; border-radius: 50%;
    border: 3px solid var(--white); display: flex; align-items: center; justify-content: center;
    color: var(--white); font-weight: 700; font-size: 18px;
    transform: translate(-50%, -50%); box-shadow: 0 2px 5px rgba(0,0,0,0.35);
  }
  .badge--1 { background: var(--teal); }
  .badge--2 { background: var(--blue-soft); }
  .badge--3 { background: var(--grey-badge); }
  .step-mark {
    position: absolute; left: 268px; top: 650px; color: var(--white);
    font-weight: 700; font-size: 17px;
  }
</style>
</head>
<body>
<main class="canvas">
  <h1 class="title">PROGRESSIVE <span class="accent">FLOW CHART</span></h1>

  <div class="brand">
    <span class="brand-dot"></span>
    <span class="brand-name">Harbor Ridge</span>
  </div>

  <svg class="flows" width="1200" height="848" viewBox="0 0 1200 848" aria-hidden="true">
    <defs>
      <marker id="head" viewBox="0 0 14 18" markerWidth="1.4" markerHeight="1.8" refX="0" refY="9" orient="auto" markerUnits="strokeWidth">
        <path d="M0,0 L14,9 L0,18 z" fill="var(--flow)"/>
      </marker>
      <linearGradient id="insuranceFade" gradientUnits="userSpaceOnUse" x1="720" y1="500" x2="944" y2="678">
        <stop offset="0" stop-color="#dcdee0" stop-opacity="0.2"/>
        <stop offset="1" stop-color="#dcdee0" stop-opacity="0.7"/>
      </linearGradient>
      <radialGradient id="trusteeFill" cx="0.3" cy="0.7" r="0.9">
        <stop offset="0" stop-color="#0094d4"/>
        <stop offset="0.6" stop-color="#00bba5"/>
        <stop offset="1" stop-color="#1af2b0"/>
      </radialGradient>
      <path id="ringArc" d="M 530,400 A 95,95 0 0 1 692,400"/>
    </defs>

    <circle class="trust-ring" cx="610" cy="457" r="125" fill="var(--ring)"/>

    <g class="flow-lines" stroke="var(--flow)" stroke-width="30" fill="none">
      <line x1="720" y1="500" x2="944" y2="678" stroke="url(#insuranceFade)" stroke-width="34"/>
      <line x1="494" y1="457" x2="430" y2="457" marker-end="url(#head)"/>
      <line x1="256" y1="678" x2="256" y2="550" marker-end="url(#head)"/>
      <line x1="331" y1="508" x2="331" y2="636" marker-end="url(#head)"/>
      <line x1="348" y1="678" x2="491.6" y2="550.8" marker-end="url(#head)"/>
      <line x1="360" y1="508" x2="550.7" y2="654.4" marker-end="url(#head)"/>
      <line x1="637" y1="575" x2="637" y2="636" marker-end="url(#head)"/>
      <line x1="519" y1="731" x2="430" y2="731" marker-end="url(#head)"/>
    </g>

    <circle class="trustee" cx="610" cy="457" r="83" fill="url(#trusteeFill)"/>
    <text x="610" y="450" text-anchor="middle" font-family="Quicksand, sans-serif" font-weight="700" font-size="24" fill="#1c2a2a">YOU</text>
    <text x="610" y="479" text-anchor="middle" font-family="Quicksand, sans-serif" font-weight="700" font-size="24" fill="#1c2a2a">TRUSTEE</text>
    <text font-family="Quicksand, sans-serif" font-weight="700" font-size="15" fill="#ffffff" letter-spacing="1">
      <textPath href="#ringArc" startOffset="50%" text-anchor="middle">LIVING TRUST</textPath>
    </text>

    <g class="flow-labels" font-family="Quicksand, sans-serif" font-weight="700" font-size="14" fill="#ffffff" text-anchor="middle">
      <text x="462" y="462">INVEST</text>
      <text transform="translate(261 594) rotate(-90)">INTEREST</text>
      <text transform="translate(336 594) rotate(-90)">INVESTMENT</text>
      <text transform="translate(434 617) rotate(-41.5)">INCOME</text>
      <text transform="translate(642 624) rotate(-90)">INCOME</text>
      <text x="456" y="736">RENT</text>
    </g>
  </svg>

  <div class="box box--strategy" style="left:208px; top:197px;">CRT</div>
  <div class="box box--strategy" style="left:519px; top:197px;">DAF</div>
  <div class="box box--strategy" style="left:832px; top:197px;">GRATS' IDGT'S</div>

  <div class="box box--bank" style="left:208px; top:402px;">
    BANK
    <span class="note">Makes Investments To<br>Real Estate + Business</span>
  </div>
  <div class="box box--entity" style="left:208px; top:678px;">REAL ESTATE<br>LLC</div>
  <div class="box box--entity box--business" style="left:519px; top:678px;">
    BUSINESS
    <span class="note">LLC - Member/ Manager<br>Corp - President</span>
  </div>
  <div class="box box--insurance" style="left:832px; top:678px;">INSURANCE</div>

  <span class="step-mark">3</span>

  <span class="badge badge--3" style="left:244px; top:197px;">3</span>
  <span class="badge badge--3" style="left:558px; top:197px;">3</span>
  <span class="badge badge--3" style="left:870px; top:197px;">3</span>
  <span class="badge badge--2" style="left:244px; top:402px;">2</span>
  <span class="badge badge--1" style="left:533px; top:384px;">1</span>
  <span class="badge badge--1" style="left:244px; top:783px;">1</span>
  <span class="badge badge--1" style="left:558px; top:783px;">1</span>
  <span class="badge badge--2" style="left:870px; top:783px;">2</span>
</main>
</body>
</html>
```